Lumacraftery 'Quiet Harbour' Book Cover Design project

I need to revise the book cover design I have for my coming book. The design I created through PixelGuild is great but the book has grown and changed so I'm looking for an alternative/option design. I can then choose later from the different options.

I need a book cover that represents the unique book I am creating.

Book Title:
The Open Meadow

Subtitle: Walking Forward Beyond Every Box

The book is targeting all readers with a special focus on same sex attracted readers. It should not have stereotypical images.

I am including a file of the book cover I have had designed. The back cover blurb, author info and author pic will remain the same. The colouring of the back cover and spine will, of course, change to match the colouring of the front cover.

The new title will be on the spine and the new title wording.

The front cover will be markedly different using the bold images and rainbow colours of the images found in the files I am uploading for you.

I am thinking of a large boldly coloured rainbow face with the title and subtitle ON the image. The image will be the whole cover. It will fill the cover as much as possible with the text added onto the pic.

The bold pictures I am including will give you the idea of what I'm looking for.

ANY of the images I've uploaded can be used as the actual front cover image OR the designer might have/find some suitable image to be used. The image is to be large and bold and fill the cover. Hopefully a positive energy.
It needs to be eye-catching and striking and bold and positive.

So...the book cover sample file I've provided can keep the back cover with completely new colouring. The front cover is completely new with new image, wording and energy.

It is to be a rainbow coloured face or figure for the cover image.

I hope that is clear enough for you. I'm very happy to discuss and clarify these ideas with the designer. Looking forward to another great PixelGuild experience.

Target Market(s)

Wide audience with special focus on Same Sex Attracted individuals

Font styles to use
Script
Other font styles liked:
• Some form of handwriting font to make the book title and text appear more personal....as if handwritten by me.

Requirements
Must have
• Boldness, Quirky, Rainbow Colour, Image to fill the cover, maybe dark cover contrasting background.
Nice to have
• A well balanced back cover especially in the area where the barcode will be placed.
Should not have
• No stereotypical images

```html
<!DOCTYPE html>
<html lang="en">
<head>
<meta charset="utf-8">
<title>The Open Meadow – Book Cover Spread</title>
<link href="https://fonts.googleapis.com/css2?family=Source+Sans+3:ital,wght@0,400;0,600;0,700;1,400;1,600&family=Gloria+Hallelujah&display=swap" rel="stylesheet">
<style>
  :root {
    --stage: #05082a;
    --cover-ink: #1d0d45;
    --spine-edge: #341a6e;
    --ink-light: #ffffff;
    --art-red: #ff3b2f;
    --art-orange: #ff8a1e;
    --art-yellow: #ffe53b;
    --art-green: #5fe06a;
    --art-blue: #2f8cff;
    --art-violet: #8a3cff;
    --art-pink: #ff4fb0;
  }
  * { margin: 0; padding: 0; box-sizing: border-box; }
  html, body { width: 1200px; height: 1200px; overflow: hidden; background: var(--stage); }
  body { position: relative; font-family: "Source Sans 3", Arial, sans-serif; color: var(--ink-light); }

  .spread { position: absolute; left: 94px; top: 250px; width: 1011px; height: 700px; }

  /* Back cover */
  .back-cover { position: absolute; left: 0; top: 0; width: 468px; height: 700px; background: var(--cover-ink); }
  .back-headline { position: absolute; left: 56px; top: 62px; width: 356px; text-align: center; font-weight: 700; font-size: 15px; line-height: 20.4px; letter-spacing: 0.2px; }
  .back-lead { position: absolute; left: 50px; top: 168px; width: 370px; }
  .back-lead em { display: block; font-style: italic; font-weight: 600; font-size: 16px; line-height: 17px; }
  .back-lead span { display: block; font-size: 10.6px; line-height: 12px; }
  .back-body { position: absolute; left: 50px; top: 210px; width: 368px; font-size: 11px; line-height: 15.2px; text-align: justify; }
  .back-body p + p { margin-top: 9px; }
  .back-quote { position: absolute; left: 50px; top: 376px; width: 368px; height: 67px; border: 1.5px solid var(--ink-light); padding: 3px 11px; font-style: italic; font-size: 8.7px; line-height: 15px; }
  .back-quote strong { display: block; font-weight: 700; }
  .back-closing { position: absolute; left: 50px; top: 457px; width: 370px; font-size: 9.5px; line-height: 11px; }
  .author-photo { position: absolute; left: 40px; top: 500px; width: 90px; height: 90px; }
  .author-bio { position: absolute; left: 156px; top: 500px; width: 262px; font-size: 10.2px; line-height: 11px; }
  .author-bio .name { font-size: 13.6px; font-weight: 700; line-height: 14px; }
  .author-bio .site { margin-top: 3px; font-size: 13px; font-weight: 700; }
  .barcode-space { position: absolute; left: 40px; top: 598px; width: 386px; height: 78px; background: var(--ink-light); }

  /* Spine */
  .spine { position: absolute; left: 468px; top: 0; width: 76px; height: 700px; background: var(--cover-ink); border-left: 1px solid var(--spine-edge); border-right: 1px solid var(--spine-edge); }
  .spine-title, .spine-author { position: absolute; left: 50%; white-space: nowrap; transform-origin: 0 0; }
  .spine-title { top: 66px; transform: rotate(90deg) translate(0, -50%); font-family: "Gloria Hallelujah", cursive; font-size: 32px; line-height: 1; }
  .spine-author { top: 476px; transform: rotate(90deg) translate(0, -50%); font-weight: 700; font-size: 21px; letter-spacing: 1px; }

  /* Front cover – full-bleed artwork */
  .front-cover { position: absolute; left: 544px; top: 0; width: 467px; height: 700px; overflow: hidden; background: var(--cover-ink); }
  .cover-art { position: absolute; inset: 0;
    background:
      radial-gradient(ellipse 45% 35% at 58% 30%, var(--art-yellow) 0%, transparent 70%),
      radial-gradient(ellipse 40% 35% at 30% 55%, var(--art-pink) 0%, transparent 70%),
      radial-gradient(ellipse 45% 35% at 75% 62%, var(--art-green) 0%, transparent 70%),
      radial-gradient(ellipse 50% 35% at 25% 90%, var(--art-blue) 0%, transparent 70%),
      radial-gradient(ellipse 45% 35% at 80% 95%, var(--art-violet) 0%, transparent 70%),
      linear-gradient(170deg, var(--art-red) 0%, var(--art-orange) 40%, var(--art-pink) 75%, var(--art-violet) 100%); }
  .front-title { position: absolute; left: 0; top: 150px; width: 467px; text-align: center; font-family: "Gloria Hallelujah", cursive; font-size: 64px; line-height: 66px; text-transform: uppercase; text-shadow: 0 2px 10px rgba(29,13,69,0.45); }
  .front-subtitle { position: absolute; left: 0; top: 370px; width: 467px; text-align: center; font-weight: 600; font-size: 21px; text-shadow: 0 1px 6px rgba(29,13,69,0.45); }
  .front-rule { position: absolute; left: 110px; top: 414px; width: 246px; height: 3px; background: var(--ink-light); }
  .front-author { position: absolute; left: 0; top: 590px; width: 467px; text-align: center; font-weight: 700; font-size: 38px; letter-spacing: 0.5px; text-shadow: 0 2px 8px rgba(29,13,69,0.45); }
</style>
</head>
<body>
  <div class="spread">
    <section class="back-cover">
      <h2 class="back-headline">IT’S IMPORTANT TO CHALLENGE OUR ACCEPTED BELIEFS AND THE STORIES WE TELL OURSELVES, INDIVIDUALLY AND AS A COMMUNITY, IF THERE IS TO BE ANY SENSE OF WHOLENESS, HAPPINESS AND FUTURE</h2>
      <div class="back-lead">
        <em>Your Rainbow is much more than the flag you wave.</em>
        <span>It is the unique and individual YOU behind the layers, labels and stories.</span>
      </div>
      <div class="back-body">
        <p>This first book by Marcus Dunleavy asks each of us to consider our accepted beliefs and personal stories as we explore the possible ways to LIVE OUR LIFE AND NOT A LABEL. Doing this require some honest inner work and a journey that will need to be passionately personal and authentically individual</p>
        <p>‘Quiet Harbour’ reminds us that a beautiful, rainbow life is more than sexuality, personality or gender or having a camp, team or tribe to belong to. It is much more than any acronym, scene or lifestyle. It’s ‘an inside job’, deeply heartfelt and courageously unique. Finding and living the YOU of YOU has boldness and power and magic in it</p>
      </div>
      <blockquote class="back-quote">“Living a meaningful, happy existence is about being true to the whole, complex, integrated person that you are and being strong enough and aware enough and reflective enough to know yourself, love yourself and be yourself” <strong>Marcus Dunleavy</strong></blockquote>
      <p class="back-closing">This simple and insightful book will help you explore ways to bravely and honestly know, love and be yourself no matter what the rest of the scene, or world, might be doing or saying or expecting.</p>
      <svg class="author-photo" role="img" aria-label="Author portrait seated beneath a tree" viewBox="0 0 90 90" preserveAspectRatio="none">
        <defs><linearGradient id="photoTone" x1="0" y1="0" x2="0" y2="1"><stop offset="0" stop-color="#4f6a2e"/><stop offset="0.6" stop-color="#6b5a36"/><stop offset="1" stop-color="#9a6a3c"/></linearGradient></defs>
        <rect width="90" height="90" fill="url(#photoTone)"/>
      </svg>
      <div class="author-bio">
        <div class="name">Marcus Dunleavy</div>
        <div>Personal Change Coach and Educator<br>LUMACRAFTERY Coaching and Wellness<br>Advocate, Activist, Writer and support for MEN WHO DATE MEN<br>and their Wholeness, Happiness and Human Rights</div>
        <div class="site">www.lumacraftery.com</div>
      </div>
      <div class="barcode-space"></div>
    </section>

    <section class="spine">
      <div class="spine-title">THE OPEN MEADOW</div>
      <div class="spine-author">MARCUS DUNLEAVY</div>
    </section>

    <section class="front-cover">
      <div class="cover-art" role="img" aria-label="Full-bleed bold rainbow-coloured painted figure in red, orange, yellow, green, blue, violet and pink brushstrokes"></div>
      <h1 class="front-title">The Open<br>Meadow</h1>
      <p class="front-subtitle">Walking Forward Beyond Every Box</p>
      <div class="front-rule"></div>
      <p class="front-author">MARCUS DUNLEAVY</p>
    </section>
  </div>
</body>
</html>
```